Web Site

Target Market(s)

CEOs and International Sales & Marketing Directors of International Companies who wish to expand their business reach to Dubai and the Middle East and are looking for a local professional partner to work with.

Requirements
Must have
• Creativity is key. We don't want the normal standard boxes of text and boxes of pics. Be as creative as you like.
Nice to have
• (This is only a suggestion, we welcome your creativity)
- The center of all pages could be large rotating pictures which display professional corporate men/women working in an office, images of Dubai, the UAE, skyscrapers of business towers in Dubai, ..etc.
- Images should reflect Dubai and the Arab World as a modern, fast-paced, growing modern market - Not Traditional)
Should not have
• Not so colorful, the fewer colors you use, the better.
Not Crammed or Busy
Not Traditional but modern

```html
<!DOCTYPE html>
<html lang="en">
<head>
<meta charset="utf-8">
<title>Kestrel Group</title>
<link href="https://fonts.googleapis.com/css2?family=Open+Sans:wght@400;600;700&display=swap" rel="stylesheet">
<style>
:root{
  --red:#9b1f1f;
  --dark:#333333;
  --ink:#2b2b2b;
  --body:#555555;
  --line:#d9d9d9;
  --nav-bg:#f4f4f4;
  --white:#ffffff;
}
*{margin:0;padding:0;box-sizing:border-box}
html,body{width:1200px;height:1084px;overflow:hidden;background:var(--white)}
body{font-family:"Open Sans",Arial,sans-serif;color:var(--ink);position:relative}
.page{position:relative;width:1200px;height:1084px}

.brand{position:absolute;left:177px;top:58px;display:flex;align-items:center;gap:10px}
.brand-square{width:14px;height:14px;background:var(--red)}
.brand-name{font-size:30px;font-weight:600;color:var(--ink);letter-spacing:1px}

.helpline{position:absolute;left:846px;top:80px;display:flex;gap:14px;align-items:flex-start}
.helpline svg{margin-top:8px}
.helpline-title{font-size:19px;color:#333;line-height:24px}
.helpline-number{font-size:17px;color:#444;line-height:23px}

.main-nav{position:absolute;left:167px;top:165px;width:864px;height:43px;background:var(--nav-bg);border:1px solid #c9c9c9;display:flex;z-index:2}
.nav-home{width:50px;height:41px;background:var(--red);display:flex;align-items:center;justify-content:center}
.nav-item{height:41px;display:flex;align-items:center;justify-content:center;font-size:14px;color:#333;border-right:1px solid #d3d3d3}
.nav-search{position:absolute;left:672px;top:5px;width:179px;height:31px;background:#fff;border:1px solid #bdbdbd;border-radius:2px;display:flex;align-items:center;padding-left:8px}

.submenu{position:absolute;left:317px;top:216px;width:199px;background:#f1f1f1;z-index:3;padding-bottom:4px}
.submenu li{list-style:none;height:27px;line-height:27px;padding-left:9px;font-size:13px;color:#333}
.submenu li.active{background:var(--red);color:#fff}

.hero{position:absolute;left:167px;top:207px;width:864px;height:315px;border:1px solid #c9c9c9;overflow:hidden;
  background:linear-gradient(180deg,#c8dbe6 0%,#b4c9d3 35%,#8f9ea4 62%,#d9dee0 78%,#6f8a8c 90%,#4d6466 100%)}
.news-tag{position:absolute;right:26px;top:175px;width:182px;height:46px;background:var(--red);color:#fff;font-size:18px;font-weight:600;display:flex;align-items:center;justify-content:center}
.news-text{position:absolute;right:26px;top:221px;background:#1f1f1f;color:#fff;font-size:13px;font-weight:600;line-height:17px;padding:9px 10px;white-space:nowrap}

.welcome{position:absolute;left:177px;top:533px;width:690px}
.welcome h1{font-size:19px;font-weight:600;color:#222;margin-bottom:8px}
.welcome p{font-size:11.3px;line-height:18px;color:var(--body)}
.btn{position:absolute;display:flex;align-items:center;justify-content:center;color:#fff;font-size:13px;border-radius:2px}
.btn-red{left:900px;top:589px;width:121px;height:44px;background:var(--red)}
.divider{position:absolute;left:177px;top:657px;width:847px;height:1px;background:var(--line)}

.feature{position:absolute;top:676px;width:265px}
.feature h2{font-size:15px;font-weight:600;color:#222;margin-bottom:10px}
.feature p{font-size:11px;line-height:18px;color:var(--body);height:72px;overflow:hidden}
.feature .btn{position:static;width:121px;height:44px;background:var(--dark);margin-top:22px}

.footer{position:absolute;left:0;top:906px;width:1200px;height:178px;background:var(--dark);color:#fff}
.footer-col{position:absolute;top:36px}
.footer-col h3{font-size:16px;font-weight:600;padding-bottom:10px;border-bottom:1px solid #bdbdbd;width:215px}
.contact-list{list-style:none;margin-top:14px}
.contact-list li{display:flex;align-items:center;gap:12px;font-size:11px;height:25px}
.contact-list b{font-weight:700}
.footer-col p{font-size:11px;line-height:18px;margin-top:14px;width:240px}
.footer-col a{color:#fff;font-weight:700;text-decoration:none;font-size:11px}
.footer-brand{font-size:22px;font-weight:600;color:#e6e6e6;letter-spacing:1px;margin-top:-4px;height:36px}
.social{position:absolute;left:178px;top:168px;display:flex;gap:16px}
.social span{width:24px;height:24px;border-radius:50%;background:#555}
</style>
</head>
<body>
<div class="page">

  <div class="brand"><span class="brand-square"></span><span class="brand-name">Kestrel Group</span></div>

  <div class="helpline">
    <svg width="20" height="28" viewBox="0 0 20 28"><path d="M5 1l4 6-3 3c1 4 3 7 6 10l3-2 4 5-4 4C6 24 1 14 2 4z" fill="#444"/></svg>
    <div>
      <div class="helpline-title">Call Us For Help</div>
      <div class="helpline-number">00971 4 5550142</div>
    </div>
  </div>

  <nav class="main-nav">
    <div class="nav-home"><svg width="16" height="15" viewBox="0 0 16 15"><path d="M8 0L0 7h2v8h4v-5h4v5h4V7h2z" fill="#fff"/></svg></div>
    <div class="nav-item" style="width:99px">About Us</div>
    <div class="nav-item" style="width:146px">About Companies</div>
    <div class="nav-item" style="width:102px">Careers</div>
    <div class="nav-item" style="width:126px">Enquiry Form</div>
    <div class="nav-item" style="width:92px;border-right:none">Contact</div>
    <div class="nav-search"><svg width="15" height="15" viewBox="0 0 15 15"><circle cx="6" cy="6" r="4.5" stroke="#777" stroke-width="1.8" fill="none"/><path d="M9.5 9.5l4 4" stroke="#777" stroke-width="2"/></svg></div>
  </nav>

  <div class="hero" role="img" aria-label="Photo of a Dubai marina with skyscrapers and moored yachts">
    <div class="news-tag">2012 Dubai News</div>
    <div class="news-text">Lorem ipsum dolor sit amet, consectetur<br>adipisicing elit, sed do eiusmod tempor.</div>
  </div>

  <ul class="submenu">
    <li class="active">Kestrel Real Estate</li>
    <li>Marotec</li>
    <li>Kestech</li>
    <li>Kestrel Mortgage Brokers</li>
    <li>K.Build</li>
    <li>Kestrel Telecom</li>
  </ul>

  <section class="welcome">
    <h1>Welcome To Kestrel Group!</h1>
    <p>Kestrel is synonymous with innovation and quality. We aim to be an intergral part of the lves of our customers, providing them with convenience and flexibility. By evaluating their needs and designing solutions to cater to these needs, Kestrel aims to remain responsible, original and ahead of times. In an increasingly connected worlds, Kestrel has always been a pioneer in introducing unique value added services and outsourcing solutions to the Middle Eastern consumer.</p>
  </section>
  <div class="btn btn-red">Read More</div>
  <div class="divider"></div>

  <section class="feature" style="left:177px">
    <h2>Our Vision</h2>
    <p>To be a regionally renowned, market-focused, customer centred brand that delivers technologically innovative solutions with excellent value for customers and stake holders, consistently outperforming.</p>
    <div class="btn">Read More</div>
  </section>
  <section class="feature" style="left:465px">
    <h2>Our Mission</h2>
    <p>We are a market-focused, process-centered organization that develops and delivers innovative solutions to our customers, consistently outperforms our peers, produces predictable earnings for our partners.</p>
    <div class="btn">Read More</div>
  </section>
  <section class="feature" style="left:753px">
    <h2>Our Divisions</h2>
    <p>We have variation sub-divisions of Kestrel Group, we provide any services that you want so we can easily help you out from your problem and give you the solutions.</p>
    <div class="btn">Read More</div>
  </section>

  <footer class="footer">
    <div class="footer-col" style="left:178px">
      <h3>Contact Details</h3>
      <ul class="contact-list">
        <li><svg width="12" height="14" viewBox="0 0 12 14"><path d="M6 0a5 5 0 0 0-5 5c0 4 5 9 5 9s5-5 5-9a5 5 0 0 0-5-5zm0 7a2 2 0 1 1 0-4 2 2 0 0 1 0 4z" fill="#fff"/></svg><span><b>P.O.BOX :</b> 7310, Dubai , UAE</span></li>
        <li><svg width="12" height="14" viewBox="0 0 20 28"><path d="M5 1l4 6-3 3c1 4 3 7 6 10l3-2 4 5-4 4C6 24 1 14 2 4z" fill="#fff"/></svg><span><b>Telephone :</b> 00971 4 5550142</span></li>
        <li><svg width="13" height="10" viewBox="0 0 13 10"><rect width="13" height="10" fill="#fff"/><path d="M0 0l6.5 5L13 0" stroke="#333" stroke-width="1.3" fill="none"/></svg><span><b>Email :</b> contact@kestrelgroup.com</span></li>
      </ul>
    </div>
    <div class="footer-col" style="left:465px">
      <h3>Careers Opportunity</h3>
      <p>Lorem ipsum dolor sit amet, consectetur adipisicing elit, sed do eiusmod tempor incididunt ut labore et dolore magna aliqua.</p>
      <a>Read more &gt;</a>
    </div>
    <div class="footer-col" style="left:751px;top:38px">
      <div class="footer-brand">Kestrel Group</div>
      <p style="margin-top:8px">A little bit about KESTREL GROUP, we are solid team that build the solutions step by step for you and make your life better.</p>
    </div>
    <div class="social"><span></span><span></span><span></span></div>
  </footer>

</div>
</body>
</html>
```